High end wine label at Austrian Winery

We are a traditional winery in Austria in region Burgenland. We are looking for a relaunch of our current wine label for our [vantor] series. It's a high end wine series at an upper price range. At the moment we have just two kinds of the label, one white one for the white wines and one black one for the red wines. This is a series of wine, white, red, sweet, sparkling and a top wine categories. So we need the same label, but in 4 different ways to distinguish the wines plus the sparkling. Maybe in color, patterns, ... or something else. The label should be very simple, including our new logo. It's also possible to make one label but we can splitting two parts of the label. The size of the label does not matter, need not be the same as now. It's a bit higher than a normal bottle. Additionally we need a back label with wine description and the wine dates on it.

Target Market(s)

private consumers and restaurants, no retailers

Colors

Designer to choose colors to be used in the design.

Requirements
Must have
• simple label with 4 different categories (red, white, sweet, top) plus Frizzante label, new logo integrated, high end label. Just logo, grape variety and [vantor] as text on the front label as text
Nice to have
• It's just good, if there'sa possibility to have different colors of each grape variety (about 10 different), but all the same style. top Wines should have an extraordinary design, but familiar with the others
Should not have
• no cheap look

```html
<!DOCTYPE html>
<html lang="en">
<head>
<meta charset="utf-8">
<title>Halden – [vantor] label series</title>
<link rel="stylesheet" href="https://fonts.googleapis.com/css2?family=Cinzel:wght@400;600&family=PT+Sans:wght@400&display=swap">
<style>
  :root {
    --page: #ffffff;
    --strip: #ffffff;
    --strip-ink: #111111;
    --night: #25272b;
    --slate: #7d8f9a;
    --coal: #0c0c0c;
    --serif: "Cinzel", "Times New Roman", serif;
    --sans: "PT Sans", Arial, sans-serif;
  }
  * { box-sizing: border-box; margin: 0; padding: 0; }
  html, body { width: 1200px; height: 524px; overflow: hidden; background: var(--page); }
  .series { position: relative; width: 1200px; height: 524px; }

  .label { position: absolute; top: 32px; width: 168px; height: 462px; }
  .label__art {
    position: absolute; left: 0; top: 0; width: 100%; height: 358px;
    background: var(--art);
  }
  .label__seal {
    position: absolute; left: 20px; top: 144px; width: 128px; height: 128px;
    border-radius: 50%; background: var(--seal-fill);
    border: 4px solid var(--seal-ring);
  }
  .label__brand {
    position: absolute; left: 0; top: 280px; width: 100%;
    text-align: center; font-family: var(--serif); font-weight: 600;
    font-size: 29px; letter-spacing: 3px; line-height: 1; color: var(--brand-ink);
  }
  .label__tagline {
    position: absolute; left: 0; top: 314px; width: 100%;
    text-align: center; font-family: var(--sans); font-weight: 400;
    font-size: 10px; letter-spacing: 1.4px; line-height: 1; color: var(--tag-ink);
  }
  .label__strip {
    position: absolute; left: 0; top: 358px; width: 100%; height: 44px;
    background: var(--strip); color: var(--strip-ink);
    border-top: 3px solid var(--rule); border-bottom: 3px solid var(--rule);
    display: flex; flex-direction: column; align-items: center; justify-content: center;
    font-family: var(--sans); text-align: center; line-height: 1.1;
  }
  .label__variety { font-size: 14px; letter-spacing: 0.3px; }
  .label__sub { font-size: 9px; letter-spacing: 0.3px; }
  .label__range { font-size: 9px; letter-spacing: 0.4px; text-transform: uppercase; }
  .label__foot {
    position: absolute; left: 0; top: 404px; width: 100%; height: 58px;
    background: var(--art-foot);
  }

  .label--welschriesling {
    left: 34px;
    --art: linear-gradient(180deg, #2b2d31, #222428 60%, #2a2c30);
    --art-foot: linear-gradient(180deg, #2a2c30, #232529);
    --seal-fill: var(--night); --seal-ring: var(--slate);
    --brand-ink: #ffffff; --tag-ink: #8a969e; --rule: #8ea2ae;
  }
  .label--spaetlese {
    left: 221px;
    --art: linear-gradient(180deg, #74899a, #5e7585 45%, #566c7b);
    --art-foot: linear-gradient(180deg, #6a8090, #5b7282);
    --seal-fill: #4f6573; --seal-ring: #ffffff;
    --brand-ink: #343a40; --tag-ink: #ffffff; --rule: #2c2f33;
  }
  .label--pinot-blanc {
    left: 417px;
    --art: linear-gradient(180deg, #d5dbdf, #b8c3ca 40%, #eef0f1 75%, #e2e6e9);
    --art-foot: linear-gradient(180deg, #e0e4e7, #cfd6db);
    --seal-fill: #bcc6cd; --seal-ring: var(--slate);
    --brand-ink: #202224; --tag-ink: #7f8e98; --rule: #8d9aa2;
  }
  .label--gruener-veltliner {
    left: 610px;
    --art: linear-gradient(180deg, #d6d6d3, #e6e6e3 45%, #cfcfcb 80%, #deded9);
    --art-foot: linear-gradient(180deg, #e2e2de, #d2d2ce);
    --seal-fill: #dadad6; --seal-ring: #9b9b9b;
    --brand-ink: #1c1c1c; --tag-ink: #8d8d8d; --rule: #a3a3a3;
  }
  .label--blaufraenkisch {
    left: 802px;
    --art: linear-gradient(180deg, #3c3c3c, #6b6b6b 35%, #5a5a5a 55%, #bdbdbd 85%, #8c8c8c);
    --art-foot: linear-gradient(180deg, #9a9a9a, #d8d8d8 60%, #b0b0b0);
    --seal-fill: #4e4e4e; --seal-ring: #0d0d0d;
    --brand-ink: #101010; --tag-ink: #1a1a1a; --rule: #111111;
  }
  .label--selegd-cuvee {
    left: 995px; height: 470px;
    --art: linear-gradient(180deg, #4a4a4a, #1b1b1b 30%, #151515 70%, #2a2a2a);
    --art-foot: linear-gradient(180deg, #2e2e2e, #4d4d4d);
    --seal-fill: #141414; --seal-ring: #ffffff;
    --brand-ink: #ffffff; --tag-ink: #d7d7d7; --rule: #ffffff;
    --strip: var(--coal); --strip-ink: #ffffff;
  }
  .label--selegd-cuvee .label__art { height: 364px; }
  .label--selegd-cuvee .label__seal { top: 148px; }
  .label--selegd-cuvee .label__brand { top: 286px; }
  .label--selegd-cuvee .label__tagline { top: 320px; }
  .label--selegd-cuvee .label__strip { top: 364px; height: 46px; border-width: 2px; }
  .label--selegd-cuvee .label__foot { top: 412px; height: 58px; }
  .label--selegd-cuvee .label__variety { font-size: 15px; }
</style>
</head>
<body>
<main class="series">

  <article class="label label--welschriesling">
    <div class="label__art" role="img" aria-label="Dark charcoal texture with a fine diamond line pattern"></div>
    <div class="label__seal"></div>
    <p class="label__brand">HALDEN</p>
    <p class="label__tagline">ESTATE OF BURGENLAND</p>
    <div class="label__strip">
      <p class="label__variety">WELSCHRIESLING</p>
      <p class="label__range">[vantor]</p>
    </div>
    <div class="label__foot" role="img" aria-label="Dark charcoal texture continuing below the band"></div>
  </article>

  <article class="label label--spaetlese">
    <div class="label__art" role="img" aria-label="Slate blue watercolour texture with a fine diamond line pattern"></div>
    <div class="label__seal"></div>
    <p class="label__brand">HALDEN</p>
    <p class="label__tagline">ESTATE OF BURGENLAND</p>
    <div class="label__strip">
      <p class="label__variety">SPÄTLESE</p>
      <p class="label__sub">TRAMINER</p>
      <p class="label__range">[vantor]</p>
    </div>
    <div class="label__foot" role="img" aria-label="Slate blue texture continuing below the band"></div>
  </article>

  <article class="label label--pinot-blanc">
    <div class="label__art" role="img" aria-label="Pale blue-grey cloud texture with a fine diamond line pattern"></div>
    <div class="label__seal"></div>
    <p class="label__brand">HALDEN</p>
    <p class="label__tagline">ESTATE OF BURGENLAND</p>
    <div class="label__strip">
      <p class="label__variety">PINOT BLANC</p>
      <p class="label__range">[vantor]</p>
    </div>
    <div class="label__foot" role="img" aria-label="Pale cloud texture continuing below the band"></div>
  </article>

  <article class="label label--gruener-veltliner">
    <div class="label__art" role="img" aria-label="Light grey cloud texture with a fine diamond line pattern"></div>
    <div class="label__seal"></div>
    <p class="label__brand">HALDEN</p>
    <p class="label__tagline">ESTATE OF BURGENLAND</p>
    <div class="label__strip">
      <p class="label__variety">GRÜNER VELTLINER</p>
      <p class="label__range">[vantor]</p>
    </div>
    <div class="label__foot" role="img" aria-label="Light grey cloud texture continuing below the band"></div>
  </article>

  <article class="label label--blaufraenkisch">
    <div class="label__art" role="img" aria-label="Black and grey ink wash texture with a fine diamond line pattern"></div>
    <div class="label__seal"></div>
    <p class="label__brand">HALDEN</p>
    <p class="label__tagline">ESTATE OF BURGENLAND</p>
    <div class="label__strip">
      <p class="label__variety">BLAUFRÄNKISCH</p>
      <p class="label__range">[vantor]</p>
    </div>
    <div class="label__foot" role="img" aria-label="Grey ink wash texture continuing below the band"></div>
  </article>

  <article class="label label--selegd-cuvee">
    <div class="label__art" role="img" aria-label="Deep black smoke texture with a fine diamond line pattern"></div>
    <div class="label__seal"></div>
    <p class="label__brand">HALDEN</p>
    <p class="label__tagline">ESTATE OF BURGENLAND</p>
    <div class="label__strip">
      <p class="label__variety">SELEGD CUVÉE</p>
      <p class="label__range">[vantor]</p>
    </div>
    <div class="label__foot" role="img" aria-label="Black smoke texture continuing below the band"></div>
  </article>

</main>
</body>
</html>
```